Kestrel Plumbing Solutions

This is for my new plumbing company, I have attached an example of what I’m going for but want it to look better.

Target Market(s)

Home owners, real estate, etc.

Industry/Entity Type

Plumbing

• As per my logo and other examples uploaded

Colors

Designer to choose colors to be used in the design.

Requirements
Must have
• Must include my logo provided and similar to my flyer I have attached but better

```html
<!DOCTYPE html>
<html lang="en">
<head>
<meta charset="utf-8">
<title>Kestrel Plumbing Solutions – Flyer</title>
<link href="https://fonts.googleapis.com/css2?family=Montserrat:wght@400;500;800;900&display=swap" rel="stylesheet">
<style>
  :root{
    --ink:#333333;
    --brand-blue:#6396e6;
    --paper:#ffffff;
    --photo-deep:#1e3f86;
    --photo-mid:#3f6fcf;
    --photo-light:#9fb8e0;
    --photo-accent:#e8c624;
  }
  *{margin:0;padding:0;box-sizing:border-box}
  html,body{width:860px;height:1200px;overflow:hidden;background:var(--paper)}
  body{font-family:'Montserrat',sans-serif;color:var(--ink)}
  .flyer{position:relative;width:860px;height:1200px;overflow:hidden;background:var(--paper)}
  .hero{position:absolute;left:0;top:0}
  .brand{position:absolute;left:50px;top:128px;color:var(--brand-blue);font-weight:800;line-height:1}
  .brand__name{display:block;font-size:62px;letter-spacing:-1px}
  .brand__tag{display:block;font-size:19px;margin-top:8px;letter-spacing:.5px}
  .brand-rule{position:absolute;left:50px;top:288px;width:232px;height:4px;background:var(--brand-blue)}
  .intro{position:absolute;left:53px;top:318px;color:var(--paper);font-size:15px;font-weight:500;line-height:19px}
  .offer{position:absolute;left:561px;top:422px;width:260px;text-align:center;color:var(--paper)}
  .offer__lead{font-size:23px;font-weight:400;line-height:28px}
  .offer__value{color:var(--brand-blue);font-weight:900;font-size:29px;line-height:34px;margin-top:2px}
  .services-title{position:absolute;left:0;top:619px;width:377px;height:56px;background:var(--ink);border-radius:0 28px 28px 0;color:var(--paper);font-size:29px;font-weight:500;padding-left:56px;line-height:56px}
  .divider{position:absolute;top:703px;width:4px;height:402px;background:var(--ink)}
  .service{position:absolute;width:260px;text-align:center;font-size:18px;font-weight:500;line-height:21px;color:var(--ink)}
  .service__icon{display:block;margin:0 auto 8px;width:65px;height:65px}
  .footer{position:absolute;left:0;top:1105px;width:860px;height:95px;background:var(--ink);color:var(--paper)}
  .contact{position:absolute;top:22px;font-size:13px;font-weight:500;text-align:center}
  .contact svg{display:block;margin:0 auto 6px}
  .contact--social{font-size:17px}
  .social-dot{display:block;width:16px;height:16px;border-radius:50%;background:var(--brand-blue);margin:0 auto 6px}
</style>
</head>
<body>
<main class="flyer">
  <svg class="hero" width="860" height="820" viewBox="0 0 860 820">
    <defs>
      <linearGradient id="photoTone" x1="0" y1="0" x2="1" y2="1">
        <stop offset="0" stop-color="var(--photo-mid)"/>
        <stop offset=".45" stop-color="var(--photo-deep)"/>
        <stop offset=".62" stop-color="var(--photo-accent)" stop-opacity=".7"/>
        <stop offset=".75" stop-color="var(--photo-deep)"/>
        <stop offset="1" stop-color="var(--photo-light)"/>
      </linearGradient>
    </defs>
    <rect x="0" y="380" width="860" height="434" fill="var(--brand-blue)"/>
    <path d="M300,0 H860 V260 L560,520 Q525,555 485,530 L270,395 Z" fill="var(--paper)" stroke="var(--paper)" stroke-width="40" stroke-linejoin="round"/>
    <path role="img" aria-label="Photo of blue industrial pipework and valves with a yellow pipe over a polished floor" d="M300,0 H860 V260 L560,520 Q525,555 485,530 L270,395 Z" fill="url(#photoTone)"/>
    <path d="M372,-10 Q520,170 478,228 L212,548 Q168,595 112,575 L0,540" fill="none" stroke="var(--ink)" stroke-width="4"/>
    <path d="M0,0 H372 L452,185 Q462,205 446,222 L190,510 Q150,550 105,530 L0,483 Z" fill="var(--ink)"/>
    <rect x="578" y="400" width="226" height="226" rx="38" transform="rotate(45 691 513)" fill="var(--paper)"/>
    <rect x="589" y="411" width="204" height="204" rx="30" transform="rotate(45 691 513)" fill="var(--ink)"/>
  </svg>

  <div class="brand">
    <span class="brand__name">KESTREL</span>
    <span class="brand__tag">PLUMBING SOLUTIONS</span>
  </div>
  <div class="brand-rule"></div>
  <p class="intro">Your local reliable Sydney plumber<br>Specialising in all aspects of<br>Plumbing, Drainage &amp;<br>Gas Maintenance.</p>

  <div class="offer">
    <p class="offer__lead">Mention<br>this flyer<br>to receive</p>
    <p class="offer__value">15%<br>DISCOUNT</p>
  </div>

  <h2 class="services-title">OURS SERVICES :</h2>

  <div class="divider" style="left:278px"></div>
  <div class="divider" style="left:557px"></div>

  <div class="service" style="left:30px;top:694px">
    <svg class="service__icon" viewBox="0 0 65 65"><circle cx="32.5" cy="32.5" r="32.5" fill="var(--ink)"/><path d="M20,22 q2,-4 6,-3 l3,6 -3,3 q3,7 10,10 l3,-3 6,3 q1,4 -3,6 q-20,-2 -22,-22z" fill="none" stroke="#fff" stroke-width="2"/><text x="40" y="28" fill="#fff" font-size="14" font-weight="500" font-family="Montserrat,sans-serif">24</text></svg>
    EMERGENCY<br>PLUMBING
  </div>
  <div class="service" style="left:289px;top:694px">
    <svg class="service__icon" viewBox="0 0 65 65"><circle cx="32.5" cy="32.5" r="32.5" fill="var(--ink)"/><path d="M20,22 h12 v18 q0,6 6,6 q6,0 6,-6 v-6 M16,19 v6 M44,30 h5" fill="none" stroke="#fff" stroke-width="2"/></svg>
    PLUMBING<br>MAINTENANCE
  </div>
  <div class="service" style="left:565px;top:694px">
    <svg class="service__icon" viewBox="0 0 65 65"><circle cx="32.5" cy="32.5" r="32.5" fill="var(--ink)"/><path d="M28,16 h10 v14 q0,6 -6,6 h-10 M22,32 v8 M30,44 l2,4 M38,42 l3,5" fill="none" stroke="#fff" stroke-width="2"/></svg>
    DRAINAGE<br>MAINTENANCE
  </div>

  <div class="service" style="left:30px;top:829px">
    <svg class="service__icon" viewBox="0 0 65 65"><circle cx="32.5" cy="32.5" r="32.5" fill="var(--ink)"/><circle cx="32.5" cy="32.5" r="15" fill="none" stroke="#fff" stroke-width="2"/><path d="M32.5,24 q6,6 4,11 q-2,4 -4,4 q-5,0 -5,-5 q0,-5 5,-10z" fill="none" stroke="#fff" stroke-width="2"/></svg>
    GAS<br>MAINTENANCE
  </div>
  <div class="service" style="left:289px;top:829px">
    <svg class="service__icon" viewBox="0 0 65 65"><circle cx="32.5" cy="32.5" r="32.5" fill="var(--ink)"/><rect x="25" y="17" width="15" height="26" rx="5" fill="none" stroke="#fff" stroke-width="2"/><path d="M32.5,27 q3,4 0,7 q-3,-3 0,-7z M20,46 h25" fill="none" stroke="#fff" stroke-width="2"/></svg>
    HOT WATER<br>SYSTEMS
  </div>
  <div class="service" style="left:565px;top:829px">
    <svg class="service__icon" viewBox="0 0 65 65"><circle cx="32.5" cy="32.5" r="32.5" fill="var(--ink)"/><path d="M16,28 h16 v8 h-16z M32,31 h6 v6 M38,20 l8,14 h-16z M38,42 q2,3 0,5 q-2,-2 0,-5z" fill="none" stroke="#fff" stroke-width="2"/></svg>
    LEAKING<br>FIXTURES
  </div>

  <div class="service" style="left:30px;top:964px">
    <svg class="service__icon" viewBox="0 0 65 65"><circle cx="32.5" cy="32.5" r="32.5" fill="var(--ink)"/><path d="M22,18 q14,0 14,14 v6 M30,18 v8 M18,44 q4,-3 8,0 q4,3 8,0 q4,-3 8,0" fill="none" stroke="#fff" stroke-width="2"/></svg>
    BLOCKED SEWER<br>&amp; STORMWATER
  </div>
  <div class="service" style="left:289px;top:964px">
    <svg class="service__icon" viewBox="0 0 65 65"><circle cx="32.5" cy="32.5" r="32.5" fill="var(--ink)"/><path d="M32.5,44 q-12,-10 -12,-18 a12,12 0 0 1 24,0 q0,8 -12,18z" fill="none" stroke="#fff" stroke-width="2"/><rect x="26" y="22" width="13" height="9" rx="2" fill="none" stroke="#fff" stroke-width="2"/><ellipse cx="32.5" cy="47" rx="12" ry="3" fill="none" stroke="#fff" stroke-width="2"/></svg>
    CAMERA<br>&amp; LOCATING
  </div>
  <div class="service" style="left:565px;top:964px">
    <svg class="service__icon" viewBox="0 0 65 65"><circle cx="32.5" cy="32.5" r="32.5" fill="var(--ink)"/><rect x="19" y="18" width="27" height="29" rx="2" fill="none" stroke="#fff" stroke-width="2"/><path d="M19,24 h27 M24,30 h17" fill="none" stroke="#fff" stroke-width="2"/><circle cx="32.5" cy="39" r="4" fill="none" stroke="#fff" stroke-width="2"/></svg>
    TMV<br>MAINTENANCE
  </div>

  <footer class="footer">
    <div class="contact" style="left:52px">
      <svg width="20" height="20" viewBox="0 0 20 20"><path d="M3,4 q1,-3 4,-2 l2,4 -2,2 q2,4 5,5 l2,-2 4,2 q1,3 -2,4 q-13,-1 -13,-13z" fill="var(--brand-blue)"/></svg>
      0491 570 156
    </div>
    <div class="contact" style="left:225px;width:290px">
      <svg width="22" height="16" viewBox="0 0 22 16"><rect x="0" y="0" width="22" height="16" rx="1" fill="var(--brand-blue)"/><path d="M1,1 l10,8 10,-8" fill="none" stroke="var(--ink)" stroke-width="2"/></svg>
      HELLO@KESTRELPLUMBING.EXAMPLE
    </div>
    <div class="contact contact--social" style="left:570px;width:250px">
      <span class="social-dot"></span>
      @KestrelPlumbingSolutions
    </div>
  </footer>
</main>
</body>
</html>
```